Nice craft box with banderole or sticker

We want to get a packaging box design for the 3D puzzle. The packaging is craft paper print black or white, wrap with a banderole or wrap with a stikcer. This box should be designed in a minimalist style as much as possible, as shown in the attached file. Only the product photos are in color, and the colors of the box and packaging are relatively simple. The color of the banderole or adhesive should be suitable. Products of different colors can be placed on without conflict. If you have better ideas, it's also possible. our product name is 3D paper puzzle or 3D cardboard Model. it have animal puzzles, like birds, insect ,wild animal. it is for young chirdren. 5-12 years old. the design also can be similar as our file, but it should be better than it.

The box size is about : 12*19*1.2CM, Attach is some packing design ideal and our logo.
we like nice font for the text. and 1-3 nice icon.

We like more nice design. It can attract the eyes. We hope all items can be use same banderole, and just put different animal photo on it.

Also You can visit our website: www.velmaro.com. you can kow how about our product.

We attach 3 items photo. You can choose one to make the design. Our product is DIY, education. Animal with scene

Target Market(s)

Europe,Janpan,USA

Requirements
Must have
• Text is black for the craft box. nice color for the banderole or sticker.
Nice to have
• nice icon.
Should not have
• craft box should not be very colorful.

```html
<!DOCTYPE html>
<html lang="en">
<head>
<meta charset="utf-8">
<title>Velmaro 3D Paper Puzzle – Peacock</title>
<link href="https://fonts.googleapis.com/css2?family=Fredoka:wght@400;500;600;700&display=swap" rel="stylesheet">
<style>
  :root {
    --kraft: #9c806a;
    --sand: #ead8c9;
    --ink: #111111;
    --cocoa: #3e3029;
    --rule: #8a6f5c;
    --muted: #7a6250;
    --leaf: #adc07a;
    --teal: #27abb8;
    --slate: #364250;
    --white: #ffffff;
  }
  * { margin: 0; padding: 0; box-sizing: border-box; }
  html, body { width: 758px; height: 1200px; overflow: hidden; }
  body {
    position: relative;
    background: var(--sand);
    font-family: "Fredoka", sans-serif;
    color: var(--ink);
  }
  .kraft-top {
    position: absolute; left: 0; top: 0;
    width: 758px; height: 663px;
    background: var(--kraft);
  }
  .title-art { position: absolute; left: 0; top: 0; }
  .feature {
    position: absolute; top: 474px; width: 160px;
    text-align: center;
  }
  .feature-icon { display: block; margin: 0 auto; }
  .feature-label {
    display: block; margin-top: 11px;
    font-size: 17px; font-weight: 600; line-height: 1;
  }
  .feature-dash {
    display: block; width: 32px; height: 2px;
    background: var(--ink); margin: 13px auto 0;
  }
  .product-photo {
    position: absolute; left: 63px; top: 726px;
    width: 316px; height: 315px; border-radius: 11px;
    background: radial-gradient(circle at 50% 42%, #9fbd6c 0%, #5fae9a 32%, #e8eee6 62%, #ffffff 80%);
  }
  .product-info { position: absolute; left: 410px; top: 740px; right: 0; }
  .series {
    font-size: 25px; font-weight: 400; color: var(--cocoa); line-height: 1;
  }
  .product-name {
    font-size: 44px; font-weight: 700; color: var(--cocoa);
    line-height: 1; margin-top: 4px; letter-spacing: 0.5px;
  }
  .info-rule {
    height: 2px; background: var(--rule); margin-top: 13px;
  }
  .specs {
    list-style: none; margin-top: 17px;
    font-size: 16px; color: var(--cocoa); line-height: 26.7px;
  }
  .specs strong { font-weight: 700; }
  .swatches { position: absolute; left: 411px; top: 972px; display: flex; gap: 11px; }
  .swatch {
    width: 47px; height: 47px; border: 2px solid var(--white);
  }
  .swatch--leaf { background: var(--leaf); }
  .swatch--teal { background: var(--teal); }
  .swatch--slate { background: var(--slate); }
  .difficulty { position: absolute; left: 588px; top: 977px; }
  .difficulty-label { font-size: 13px; color: var(--cocoa); line-height: 1; }
  .difficulty svg { display: block; margin-top: 4px; }
  .dash-rule {
    position: absolute; left: 410px; top: 1040px; width: 286px;
    border-top: 2px dashed var(--rule);
  }
  .kraft-bottom {
    position: absolute; left: 0; top: 1105px;
    width: 758px; height: 95px; background: var(--kraft);
    display: flex; align-items: center; justify-content: center;
  }
  .brand-name {
    font-size: 32px; font-weight: 700; letter-spacing: 4px; color: var(--ink);
  }
</style>
</head>
<body>
  <header class="kraft-top">
    <svg class="title-art" width="758" height="663" viewBox="0 0 758 663" aria-hidden="true">
      <defs>
        <path id="arc-top" d="M 215 228 Q 379 190 543 228"/>
        <path id="arc-bottom" d="M 215 365 Q 379 395 543 365"/>
      </defs>
      <line x1="61" y1="126" x2="694" y2="126" stroke="#111" stroke-width="2"/>
      <text font-family="Fredoka, sans-serif" font-weight="600" font-size="40" fill="#111" text-anchor="middle">
        <textPath href="#arc-top" startOffset="50%">3D Paper Puzzle</textPath>
      </text>
      <g fill="none" stroke="#111" stroke-width="3.5" stroke-linejoin="round">
        <g transform="translate(283 289)">
          <path d="M0 -21 L19 -10 L19 11 L0 22 L-19 11 L-19 -10 Z"/>
          <path d="M-19 -10 L0 1 L19 -10 M0 1 L0 22"/>
        </g>
        <g transform="translate(379 289)">
          <path d="M0 -21 L19 -10 L19 11 L0 22 L-19 11 L-19 -10 Z"/>
          <path d="M-19 -10 L0 1 L19 -10 M0 1 L0 22"/>
        </g>
        <g transform="translate(475 289)">
          <path d="M0 -21 L19 -10 L19 11 L0 22 L-19 11 L-19 -10 Z"/>
          <path d="M-19 -10 L0 1 L19 -10 M0 1 L0 22"/>
        </g>
      </g>
      <circle cx="331" cy="289" r="5.5" fill="#111"/>
      <circle cx="427" cy="289" r="5.5" fill="#111"/>
      <text font-family="Fredoka, sans-serif" font-weight="600" font-size="43" fill="#111" text-anchor="middle">
        <textPath href="#arc-bottom" startOffset="50%">Cardboard Model</textPath>
      </text>
      <line x1="62" y1="442" x2="695" y2="442" stroke="#111" stroke-width="2"/>
    </svg>

    <div class="feature" style="left:88px">
      <svg class="feature-icon" width="50" height="50" viewBox="0 0 50 50" aria-hidden="true">
        <circle cx="25" cy="25" r="23.5" fill="none" stroke="#111" stroke-width="2"/>
        <path d="M17 19 h4 a3 3 0 1 1 6 0 h4 v4 a3 3 0 1 1 0 6 v4 h-4 a3 3 0 1 0 -6 0 h-4 v-4 a3 3 0 1 0 0 -6 Z" fill="none" stroke="#111" stroke-width="2" stroke-linejoin="round" transform="rotate(-20 25 25)"/>
      </svg>
      <span class="feature-label">Do It Yourself</span>
      <span class="feature-dash"></span>
    </div>
    <div class="feature" style="left:299px">
      <svg class="feature-icon" width="50" height="50" viewBox="0 0 50 50" aria-hidden="true">
        <circle cx="25" cy="25" r="23.5" fill="none" stroke="#111" stroke-width="2"/>
        <path d="M16 33 C14 22 22 15 34 16 C35 28 28 35 16 33 Z M16 33 L26 24" fill="none" stroke="#111" stroke-width="2" stroke-linejoin="round" stroke-linecap="round"/>
      </svg>
      <span class="feature-label">Eco-Friendly</span>
      <span class="feature-dash"></span>
    </div>
    <div class="feature" style="left:509px">
      <svg class="feature-icon" width="50" height="50" viewBox="0 0 50 50" aria-hidden="true">
        <circle cx="25" cy="25" r="23.5" fill="none" stroke="#111" stroke-width="2"/>
        <g fill="none" stroke="#111" stroke-width="2" stroke-linecap="round">
          <circle cx="16" cy="22" r="3"/>
          <circle cx="24" cy="32" r="3"/>
          <path d="M19 23 L35 25 M25 29 L27 13"/>
          <path d="M9 41 L41 9"/>
        </g>
      </svg>
      <span class="feature-label">Tool-Free</span>
      <span class="feature-dash"></span>
    </div>
  </header>

  <div class="product-photo" role="img" aria-label="Photo of the assembled cardboard peacock model with its fanned green and teal tail, surrounded by loose puzzle pieces"></div>

  <section class="product-info">
    <p class="series">Animal Series</p>
    <h1 class="product-name">Peacock</h1>
    <div class="info-rule"></div>
    <ul class="specs">
      <li>Pieces: <strong>45 pcs</strong></li>
      <li>Size: 7x10 cm</li>
      <li>Material: Paper Cardboard</li>
      <li>Color: Green, Blue, Black</li>
    </ul>
  </section>

  <div class="swatches">
    <span class="swatch swatch--leaf"></span>
    <span class="swatch swatch--teal"></span>
    <span class="swatch swatch--slate"></span>
  </div>

  <div class="difficulty">
    <p class="difficulty-label">Difficulty</p>
    <svg width="98" height="18" viewBox="0 0 98 18" aria-label="Difficulty 4 of 5">
      <defs>
        <path id="star" d="M8 1 L10.1 6 L15.5 6.4 L11.4 9.9 L12.7 15.2 L8 12.3 L3.3 15.2 L4.6 9.9 L0.5 6.4 L5.9 6 Z"/>
      </defs>
      <use href="#star" x="0" fill="#7a6250"/>
      <use href="#star" x="20" fill="#7a6250"/>
      <use href="#star" x="40" fill="#7a6250"/>
      <use href="#star" x="60" fill="#7a6250"/>
      <use href="#star" x="80" fill="none" stroke="#7a6250" stroke-width="1"/>
    </svg>
  </div>

  <div class="dash-rule"></div>

  <footer class="kraft-bottom">
    <span class="brand-name">VELMARO</span>
  </footer>
</body>
</html>
```